Business card design needed

A laid back coffee shop that has a great feel, that becomes a bar and grill at night. We are also wanting to cater for functions etc.
The business itself is painted dark blue/charcoal and has red doors.
Would like a logo that will be recognised when seen.

Industry/Entity Type

Coffee Shop

Contact Information for Business Card

The Lantern Coffee Bar & Grill
14b Wattlebrook St
Kelmarra NSW 2318
Ph. 02 4817 6293

Logo Text

Logo styles of interest
Emblem Logo
Abstract Logo
Wordmark Logo
Requirements
Must have
• A loyalty card on the back with 2 rows of 7 stamp spaces and a place to write a name and phone number (for a draw)

```html
<!DOCTYPE html>
<html lang="en">
<head>
<meta charset="utf-8">
<title>The Lantern Coffee Bar &amp; Grill — Business &amp; Loyalty Card</title>
<link rel="stylesheet" href="https://fonts.googleapis.com/css2?family=Arimo:wght@400;700&display=swap">
<style>
  :root {
    --backdrop: #2c3034;
    --charcoal: #37444e;
    --charcoal-deep: #2c3740;
    --red: #c61f29;
    --red-deep: #a5151e;
    --red-line: #e33a42;
    --stamp: #e4e4e4;
    --white: #ffffff;
    --ink: #2a2a2a;
  }
  * { box-sizing: border-box; margin: 0; padding: 0; }
  html, body { width: 1200px; height: 900px; overflow: hidden; }
  body {
    background: var(--backdrop);
    font-family: "Arimo", Arial, sans-serif;
    position: relative;
  }
  .card {
    position: absolute;
    width: 520px;
    height: 318px;
    border-radius: 4px;
    box-shadow: 0 10px 28px rgba(0,0,0,.45);
    overflow: hidden;
  }

  /* Loyalty side */
  .loyalty-card { left: 60px; top: 120px; background: var(--charcoal); }
  .stamp-grid {
    position: absolute; left: 26px; top: 30px;
    display: grid; grid-template-columns: repeat(7, 44px); gap: 14px 12px;
  }
  .stamp { width: 44px; height: 34px; background: var(--stamp); border-radius: 2px; }
  .loyalty-brand {
    position: absolute; right: 24px; top: 118px; width: 150px;
    display: flex; align-items: center; gap: 10px;
  }
  .brand-dot { flex: none; width: 22px; height: 22px; border-radius: 50%; background: var(--red); }
  .loyalty-brand .brand-name { color: var(--white); font-size: 15px; line-height: 1.25; }
  .draw-entry {
    position: absolute; left: 26px; right: 40px; bottom: 22px; height: 34px;
    background: var(--stamp); border-radius: 17px;
    display: flex; align-items: center; gap: 8px; padding: 0 18px;
    font-size: 15px; color: var(--ink);
  }
  .draw-entry .field { flex: 1; border-bottom: 1px solid var(--ink); height: 14px; }

  /* Contact side */
  .contact-card { left: 620px; top: 120px; background: var(--red); }
  .panel {
    position: absolute; top: 14px; bottom: 14px;
    border: 2px solid var(--red-line);
    box-shadow: inset 0 0 0 2px var(--red-deep);
    border-radius: 3px;
  }
  .panel-details { left: 14px; width: 282px; }
  .panel-brand { right: 14px; width: 196px; display: flex; align-items: center; justify-content: center; }
  .holder-name { position: absolute; left: 22px; top: 26px; color: var(--white); font-size: 24px; letter-spacing: .5px; }
  .holder-role { position: absolute; left: 22px; top: 58px; color: var(--white); font-size: 12px; }
  .holder-contact { position: absolute; left: 22px; top: 80px; color: var(--white); font-size: 13px; line-height: 1.55; }
  .decor-motif {
    position: absolute; left: 22px; bottom: 40px; width: 110px; height: 80px;
    background: linear-gradient(135deg, rgba(255,255,255,.28), rgba(255,255,255,.08));
    border-radius: 3px;
  }
  .address { position: absolute; left: 22px; bottom: 14px; color: var(--white); font-size: 12px; }
  .brand-stack { display: flex; flex-direction: column; align-items: center; gap: 10px; }
  .brand-ring { width: 64px; height: 64px; border-radius: 50%; background: var(--charcoal); }
  .panel-brand .brand-name { color: var(--white); font-size: 16px; text-align: center; line-height: 1.3; }

  /* Standalone brand block */
  .brand-block {
    position: absolute; right: 50px; bottom: 40px; width: 230px;
    display: flex; flex-direction: column; align-items: center; gap: 12px;
  }
  .brand-block .brand-ring { width: 90px; height: 90px; background: var(--charcoal); border: 0; }
  .brand-block .brand-name { color: var(--white); font-size: 20px; text-align: center; line-height: 1.3; }
</style>
</head>
<body>

  <section class="card loyalty-card" aria-label="Loyalty card">
    <div class="stamp-grid">
      <span class="stamp"></span><span class="stamp"></span><span class="stamp"></span><span class="stamp"></span><span class="stamp"></span><span class="stamp"></span><span class="stamp"></span>
      <span class="stamp"></span><span class="stamp"></span><span class="stamp"></span><span class="stamp"></span><span class="stamp"></span><span class="stamp"></span><span class="stamp"></span>
    </div>
    <div class="loyalty-brand">
      <span class="brand-dot"></span>
      <span class="brand-name">The Lantern Coffee Bar &amp; Grill</span>
    </div>
    <div class="draw-entry">
      <span>Name:</span><span class="field"></span>
      <span>Phone:</span><span class="field"></span>
    </div>
  </section>

  <section class="card contact-card" aria-label="Business card">
    <div class="panel panel-details">
      <p class="holder-name">SAM WHITFIELD</p>
      <p class="holder-role">Designer</p>
      <p class="holder-contact">Phone: 02 4817 6293<br>Mail: hello@lanterncoffee.com</p>
      <div class="decor-motif" role="img" aria-label="Faint coffee cup and music notes motif"></div>
      <p class="address">14b Wattlebrook St Kelmarra NSW 2318</p>
    </div>
    <div class="panel panel-brand">
      <div class="brand-stack">
        <span class="brand-ring"></span>
        <span class="brand-name">The Lantern Coffee<br>Bar &amp; Grill</span>
      </div>
    </div>
  </section>

  <div class="brand-block">
    <span class="brand-ring"></span>
    <span class="brand-name">The Lantern Coffee<br>Bar &amp; Grill</span>
  </div>

</body>
</html>
```